Bidmo Store Banner

I have an bidmo store which displays the store name which is Mrs.Wexley's Drifting Moon-Bazaar. I want to make this store landing page look better so I want a design to be used as what bidmo calls a Store banner. I attach a pic of the visuals of the landing page of my store and I also attach a pic of another store who have set up a banner.

Colors
85cae6
6cbee2
33a6d7
0355a3
3276b5
cedeed
d6edf3
eaf1f7

```html
<!DOCTYPE html>
<html lang="en">
<head>
<meta charset="utf-8">
<title>Bidmo Store Banner – Mrs.Wexley's Drifting Moon-Bazaar</title>
<link rel="stylesheet" href="https://fonts.googleapis.com/css2?family=Hind:wght@500;600&display=swap">
<style>
  :root {
    --sheet: #757575;
    --royal: #1a62b0;
    --royal-soft: #3276b5;
    --deep: #0355a3;
    --mist: #eaf1f7;
    --white: #ffffff;
    --amber: #f5a623;
    --leaf: #5aab1e;
    --night: #0d1016;
    --badge-ink: #0355a3;
  }
  * { box-sizing: border-box; margin: 0; padding: 0; }
  html, body { width: 1200px; height: 986px; overflow: hidden; }
  body {
    background: var(--sheet);
    font-family: "Hind", "Arial", sans-serif;
    position: relative;
  }
  .banner {
    position: absolute;
    left: 61px;
    width: 1078px;
    height: 242px;
    overflow: hidden;
    box-shadow: 0 3px 6px rgba(0,0,0,.35);
  }
  .banner--gallery { top: 74px; }
  .banner--night { top: 372px; }
  .banner--light { top: 670px; background: var(--mist); }

  .photo { position: absolute; top: 0; height: 100%; }
  .photo--vase { left: 0; width: 174px; background: linear-gradient(180deg, #f1ebe1, #e7b25a 45%, #d76f1d 80%, #efe6d8); }
  .photo--pitcher { left: 174px; width: 226px; background: linear-gradient(160deg, #f3f2ef 20%, #b8dbb2 50%, #d7b45a 70%, #f1f0ec); }
  .photo--bowl { left: 400px; width: 401px; background: linear-gradient(180deg, #d9d4cc 0%, #eeebe6 30%, #2a3542 60%, #0f1418 78%, #e4e1dc 100%); }
  .photo--shade { left: 801px; width: 277px; background: radial-gradient(circle at 45% 45%, #f1eee6 0 30%, #cfc8bd 42%, #4a3a34 70%, #2d2422); }

  .name-box {
    position: absolute;
    left: 295px; top: 53px;
    width: 507px; height: 137px;
    background: var(--royal-soft);
    opacity: .96;
    display: flex; flex-direction: column; justify-content: center; align-items: center;
    color: var(--white);
    font-weight: 600;
    font-size: 42px;
    line-height: 1.4;
    text-align: center;
  }

  .photo--glasses { left: 0; width: 100%; background: linear-gradient(90deg, #0b0e14 0%, #1b222c 40%, #2a2f35 60%, #8d8f93 72%, #4a4d52 82%, #0b0e14 100%); }
  .night-title {
    position: absolute;
    left: 54px; top: 46px;
    font-weight: 600;
    font-size: 58px;
    line-height: 86px;
    color: var(--white);
  }
  .night-title .blue { color: var(--royal); }
  .night-title .amber { color: var(--amber); }
  .night-title .leaf { color: var(--leaf); }

  .photo--cases { left: 6px; top: 44px; width: 388px; height: 171px; background: linear-gradient(180deg, #7a2a22, #4e1511); border-radius: 6px; }
  .name-frame {
    position: absolute;
    left: 405px; top: 36px;
    width: 565px; height: 171px;
    background: var(--white);
    padding: 12px;
  }
  .name-frame .name-box {
    position: static;
    width: 100%; height: 100%;
    background: var(--royal);
    opacity: 1;
    font-size: 41px;
  }

  .badge {
    position: absolute;
    left: 986px; top: 10px;
    width: 81px; height: 81px;
    border-radius: 50%;
    background: var(--white);
    border: 3px solid var(--deep);
    display: flex; align-items: center; justify-content: center;
    font-weight: 600;
    font-size: 25px;
    color: var(--badge-ink);
  }
</style>
</head>
<body>
  <section class="banner banner--gallery">
    <div class="photo photo--vase" role="img" aria-label="Amber ribbed carnival glass vase"></div>
    <div class="photo photo--pitcher" role="img" aria-label="Green glass pitcher with gold bands"></div>
    <div class="photo photo--bowl" role="img" aria-label="Dark glass bowl on a pale surface"></div>
    <div class="photo photo--shade" role="img" aria-label="White marbled glass lamp shade"></div>
    <div class="name-box">
      <span>MRS.WEXLEY'S</span>
      <span>DRIFTING MOON-BAZAAR</span>
    </div>
    <div class="badge">bidmo</div>
  </section>

  <section class="banner banner--night">
    <div class="photo photo--glasses" role="img" aria-label="Textured crystal tumblers on a dark background"></div>
    <h1 class="night-title">
      <span class="blue">MRS.WEXLEY'S</span> <span class="amber">DRIFTING</span><br>
      <span>MOON</span> <span class="leaf">BAZAAR</span>
    </h1>
    <div class="badge">bidmo</div>
  </section>

  <section class="banner banner--light">
    <div class="photo photo--cases" role="img" aria-label="Two red translucent collector video cases"></div>
    <div class="name-frame">
      <div class="name-box">
        <span>MRS.WEXLEY'S</span>
        <span>DRIFTING MOON-BAZAAR</span>
      </div>
    </div>
    <div class="badge">bidmo</div>
  </section>
</body>
</html>
```